We are opening a new restaurant concept called Lanternleaf - Fresh Asian Cuisine. Will be a trendy, casual dining restaurant (somewhat similar to a QR Morvins).
I have included pics of our logo in different formats and a picture of our front menu cover and inside menu as well as our actual menu in draft format. Need 6 individual pages total and letter size. Inside cover would be a "about us" type page that describes who we are and mission statement of restaurant (script unwritten at this time), Next page would be appetizers, inside page would have entrees on left and right side of book, then noodles/rice, vegetarian, kids and dessert section, last page would be drink/cocktail menu (still in progress).

```html
<!DOCTYPE html>
<html lang="en">
<head>
<meta charset="utf-8">
<title>Lanternleaf - Fresh Asian Cuisine Menu</title>
<link href="https://fonts.googleapis.com/css2?family=Noto+Serif:wght@400;700&display=swap" rel="stylesheet">
<style>
  :root {
    --backdrop: #e4e4e6;
    --paper: #f4f3f1;
    --paper-right: #ecebe9;
    --ink: #2a2a2a;
    --ink-soft: #4a4a4a;
    --accent: #c8242b;
    --rule: #9a9a9a;
  }
  * { box-sizing: border-box; margin: 0; padding: 0; }
  html, body { width: 1200px; height: 813px; overflow: hidden; }
  body {
    background: var(--backdrop);
    font-family: "Noto Serif", Georgia, serif;
    color: var(--ink);
    display: flex;
    justify-content: center;
    align-items: center;
  }
  .spread { display: flex; width: 1140px; height: 781px; box-shadow: 0 2px 10px rgba(0,0,0,.15); }
  .page { position: relative; width: 570px; height: 100%; background: var(--paper); }
  .page--right { background: var(--paper-right); }
  .page__frame {
    position: absolute; inset: 28px;
    border: 1px dotted var(--accent);
  }
  .brand {
    position: absolute; top: 14px; left: 50%; transform: translateX(-50%);
    display: flex; align-items: center; gap: 7px;
    background: inherit; padding: 0 10px;
    font-size: 15px; font-weight: 700; color: var(--ink);
  }
  .page--left .brand { background: var(--paper); }
  .page--right .brand { background: var(--paper-right); }
  .brand__dot { width: 14px; height: 14px; border-radius: 50%; background: var(--accent); }
  .page__title {
    position: absolute; top: 58px; width: 100%; text-align: center;
    font-size: 20px; font-weight: 400; letter-spacing: 1px;
  }
  .about {
    position: absolute; top: 150px; left: 70px; right: 70px;
    font-size: 13.5px; line-height: 1.5; color: var(--ink);
  }
  .about p + p { margin-top: 18px; }
  .menu {
    position: absolute; top: 115px; left: 56px; right: 56px;
    display: grid; grid-template-columns: 1fr 1fr; gap: 0 30px;
  }
  .menu__item {
    position: relative; padding: 6px 28px 7px 0;
    border-bottom: 1px dotted var(--rule);
    min-height: 48px;
  }
  .menu__item:last-child { border-bottom: none; }
  .menu__name { font-size: 11.5px; font-weight: 700; }
  .menu__desc { font-size: 9px; line-height: 1.3; color: var(--ink-soft); }
  .menu__price { position: absolute; right: 0; top: 6px; font-size: 10px; color: var(--ink-soft); }
</style>
</head>
<body>
  <div class="spread">
    <section class="page page--left">
      <div class="page__frame">
        <div class="brand"><span class="brand__dot"></span>Lanternleaf</div>
      </div>
      <h1 class="page__title">ABOUT US</h1>
      <div class="about">
        <p>Curabitur posuere euismod vestibulum. Fusce suscipit accumsan augue quis efficitur. Duis viverra diam et dolor condimentum, ac pharetra ex maximus. Mauris dapibus bibendum lacus, in sodales nulla. Maecenas hendrerit orci felis. Pellentesque habitant morbi tristique senectus et netus et malesuada fames ac turpis egestas. Lorem ipsum dolor sit amet, consectetur adipiscing elit. Nulla elementum ante lectus, sit amet fermentum elit luctus at. Nam aliquam nisi quis tellus consequat, a suscipit urna luctus. Vestibulum ante ipsum primis in faucibus orci luctus et ultrices posuere cubilia Curae; Phasellus eget risus nec nisl gravida sagittis. Maecenas egestas lacus suscipit dolor blandit blandit. Sed mattis posuere mi, et maximus neque fringilla sed. Phasellus sagittis sapien ac dolor tincidunt eleifend.</p>
        <p>Maecenas ut nisi sed augue hendrerit fermentum in eu dui. Aenean bibendum tortor lorem, id porttitor erat auctor ut. Aenean ac quam enim. Integer lobortis eros eu dui pharetra, sit amet facilisis ipsum accumsan. Donec sed massa in urna tristique cursus at nec magna. Vivamus ultricies ultricies aliquet. Ut eu nunc non nisi vestibulum pulvinar in et ligula.</p>
        <p>Praesent elementum pulvinar ornare. Sed consequat varius orci, non vulputate ipsum luctus vitae. Quisque et pellentesque urna. Donec non ante enim. Morbi venenatis risus vel lectus mollis consectetur. Ut non ligula eget purus tempor efficitur sed sed ligula. Proin sagittis sed elit eget sagittis. Phasellus eu diam vitae erat vulputate iaculis. Sed pretium urna non accumsan vehicula.</p>
      </div>
    </section>

    <section class="page page--right">
      <div class="page__frame">
        <div class="brand"><span class="brand__dot"></span>Lanternleaf</div>
      </div>
      <h1 class="page__title">APPETIZERS</h1>
      <div class="menu">
        <div class="menu__col">
          <div class="menu__item"><div class="menu__name">Edamame</div><div class="menu__desc">Seasoned &amp; boiled soy bean</div><span class="menu__price">$4</span></div>
          <div class="menu__item"><div class="menu__name">Scallion Pancakes</div><div class="menu__desc">Traditional Chinese flatbread folded with oil and minced scallions and pan fried</div><span class="menu__price">$6</span></div>
          <div class="menu__item"><div class="menu__name">Lanternleaf Lettuce Wraps</div><div class="menu__desc">Seasoned ground chicken wrapped in lettuce and drizzled with our secret sauce</div><span class="menu__price">$8</span></div>
          <div class="menu__item"><div class="menu__name">Salt &amp; Pepper Calamari</div><div class="menu__desc">Crispy Calamari with Green &amp; red peppers and onions</div><span class="menu__price">$9</span></div>
          <div class="menu__item"><div class="menu__name">Singapore Ribs</div><div class="menu__desc">Tender baby back ribs in a sweet homemade glaze</div><span class="menu__price">$9</span></div>
          <div class="menu__item"><div class="menu__name">Spicy Bang Bang Shrimp</div><div class="menu__desc">Crispy fried shrimp tossed in our creamy spicy sauce</div><span class="menu__price">$9</span></div>
          <div class="menu__item"><div class="menu__name">Drunken Chicken</div><div class="menu__desc">Chicken, Thai chili and a house made spicy sauce</div><span class="menu__price">$8</span></div>
          <div class="menu__item"><div class="menu__name">Sichuan Spiced Beef</div><div class="menu__desc">Beef Shank, beef tripe, cilantro, peanuts and celery</div><span class="menu__price">$9</span></div>
          <div class="menu__item"><div class="menu__name">Beef Crispy Bottom Bow</div><div class="menu__desc">Pan fried crispy bottom bao, stuffed with beef, drizzled with scallion and sesame</div><span class="menu__price">$10</span></div>
          <div class="menu__item"><div class="menu__name">Crispy Mala Beef Jerky</div><div class="menu__desc">Dry fried shredded beef with fresh celery, Serrano peppers, garlic, green onion in soy sauce and peppercorn oil</div><span class="menu__price">$9</span></div>
          <div class="menu__item"><div class="menu__name">Steamed Chicken Dumplings (6)</div><div class="menu__desc">Chinese dumpling stuffed with Chicken, Shiitake mushrooms and bamboo shoots</div><span class="menu__price">$6</span></div>
        </div>
        <div class="menu__col">
          <div class="menu__item"><div class="menu__name">Red Oil Dumplings (6)</div><div class="menu__desc">Pork filled dumplings in Sichuan red oil sauce drizzled with sesame</div><span class="menu__price">$7</span></div>
          <div class="menu__item"><div class="menu__name">Pork Egg Rolls (2) $4</div><div class="menu__desc">Hand rolled with julienned veggies with our sweet n' sour mustard sauce</div><span class="menu__price">$4</span></div>
          <div class="menu__item"><div class="menu__name">Vegetarian Spring Rolls (3)</div><div class="menu__desc">Fresh rice paper roll filled with vermicelli, bean sprouts and lettuce. Served with peanut sauce</div><span class="menu__price">$4</span></div>
          <div class="menu__item"><div class="menu__name">Garlic Cucumber Salad</div><div class="menu__desc">Sliced cucumber with a garlic vinaigrette</div><span class="menu__price">$7</span></div>
          <div class="menu__item"><div class="menu__name">Lanternleaf Hot n' Sour Soup</div><div class="menu__desc">Tangy broth with Bamboo shoot, wood ear fungus, tofu, egg and carrots</div><span class="menu__price">$4</span></div>
          <div class="menu__item"><div class="menu__name">West Lake Soup</div><div class="menu__desc">Light creamy soup with ground beef, diced Shiitake mushroom, tofu, bamboo shoots, egg white and cilantro</div><span class="menu__price">$4</span></div>
        </div>
      </div>
    </section>
  </div>
</body>
</html>
```